Web Page needed for Dr. Brannock Advisory

The company works in the consultant business for processes in large projects our of engineering and construction business. We develop strategies but work also in critical projects to get them right.
The page should have a modern appearance but though a classy and luxury touch.
Updates

The project was bought in a package, logo plus web page. Now the designers do submit logos again, although the logo has been set. This part is only the web site. I changed the text to clarify it, I contacted support to put that right, but that needs an extension of minimum 7 days to catch up.

Due to the confusion in the project, it was first set up as logo project and later corrected (I have no clue how that happened, as I bought a package with logo + web, and logo is already done), there is a large delay in getting feedback. Please be so kind and extend until 31.01. In Europe there is holidays until 07.01. and I have no time to discuss the topics with my client until 10.01., than we need to feed in response and get changes done.

Logo Text

The logo is already fixed, I asked for web page.

Number of Pages Required

5+ page

Font styles to use
Sans Serif

Colors

Designer to choose colors to be used in the design.

Requirements
Must have
• Home/Start
• Lean Construction
• Lean Equipment
• Lean Design
• Lean Training
• Team
• Contact
• Imprint
Nice to have
• Darker color, luxury appearance, please integrate the logo in the attachment here.
• I would like to have a web page with animated context, such as this one here: https://quellworks.example

```html
<!DOCTYPE html>
<html lang="en">
<head>
<meta charset="utf-8">
<title>Dr. Brannock Advisory</title>
<link rel="stylesheet" href="https://fonts.googleapis.com/css2?family=Cinzel:wght@400;600&family=Montserrat:wght@600;700&family=Quicksand:wght@400;500;600&display=swap">
<style>
:root{
  --green:#8cc63f;
  --green-soft:#a6d160;
  --blue:#2e75b6;
  --blue-dark:#25609a;
  --ink:#111;
  --text:#4a4a4a;
  --mist:#eef3f9;
  --white:#fff;
}
*{margin:0;padding:0;box-sizing:border-box}
html,body{width:1200px;height:3453px;overflow:hidden;background:var(--white)}
body{position:relative;font-family:"Quicksand",sans-serif;color:var(--text)}
.abs{position:absolute}
.serif{font-family:"Cinzel",serif}
.btn{position:absolute;display:flex;align-items:center;justify-content:space-between;background:var(--blue);color:var(--white);border-radius:30px;font-family:"Cinzel",serif;font-size:17px;letter-spacing:.5px;padding:0 6px 0 20px}
.btn .arrow{width:40px;height:40px;border-radius:50%;background:var(--green);display:flex;align-items:center;justify-content:center}
.circle{position:absolute;border-radius:50%}
.photo{position:absolute;overflow:hidden}

/* nav */
.brand{left:78px;top:30px;display:flex;align-items:center;gap:10px}
.brand .mark{width:34px;height:34px;background:var(--blue);border-radius:4px}
.brand span{font-family:"Cinzel",serif;font-size:22px;color:var(--blue)}
.nav{left:473px;top:36px;display:flex;gap:22px;font-size:15px;color:var(--ink);font-weight:500}
.nav .active{position:relative}
.nav .active::before{content:"";position:absolute;left:-18px;top:-14px;width:42px;height:42px;border-radius:50%;background:var(--green);z-index:-1}

/* hero */
.hero-title{left:75px;top:226px;font-family:"Montserrat",sans-serif;font-weight:700;font-size:43px;line-height:47px;color:var(--ink)}
.hero-sub{left:79px;top:380px;font-size:16px;line-height:27px;color:#333}
.pager{left:1153px;top:290px}
.pager i{display:block;width:12px;height:12px;border-radius:50%;background:#fff;margin-bottom:12px}
.pager i.on{background:var(--white);border:3px solid var(--blue)}

/* about */
.about-mark{left:138px;top:795px;width:372px;height:365px;display:flex;align-items:center;justify-content:center;gap:16px}
.about-mark b{font-family:"Quicksand",sans-serif;font-weight:600;font-size:34px;color:var(--blue);line-height:42px}
.eyebrow{color:var(--green);font-size:18px;font-weight:500}
.h2{font-family:"Cinzel",serif;color:var(--blue);font-weight:400}
.about-copy{left:643px;top:900px;width:430px;font-size:14px;line-height:27px}
.about-copy p+p{margin-top:15px}

/* services */
.card{position:absolute;top:1444px;width:235px;height:382px;background:var(--white);border:1px solid #e8e8e8;border-radius:3px}
.card .pic{height:182px}
.card h3{font-family:"Cinzel",serif;font-weight:400;font-size:17px;color:var(--blue);margin:34px 0 0 20px}
.card p{font-size:14px;line-height:25px;margin:8px 20px 0 22px}
.card a{display:block;margin:14px 0 0 24px;color:var(--green);font-size:14px;font-weight:600;text-decoration:underline}

/* team */
.member{position:absolute;top:2012px;width:228px;height:469px;border-radius:114px;background:var(--white);box-shadow:0 6px 18px rgba(0,0,0,.08);text-align:center}
.member .face{width:188px;height:188px;border-radius:50%;margin:22px auto 0}
.member h4{font-family:"Cinzel",serif;font-weight:400;font-size:18px;color:var(--green);margin-top:42px}
.member p{font-size:14px;line-height:27px;margin:12px 18px 0}
.member .soc{width:42px;height:42px;border-radius:50%;background:var(--blue);margin:26px auto 0}

/* footer */
.f-title{font-family:"Cinzel",serif;font-size:20px;color:var(--blue);letter-spacing:.5px}
.f-list{list-style:none;font-size:14px;line-height:29.5px;color:#333}
.f-list li::before{content:"";display:inline-block;width:5px;height:5px;border-radius:50%;background:var(--blue);margin:0 16px 2px 0}
</style>
</head>
<body>

<!-- hero background -->
<div class="circle photo" style="left:623px;top:-34px;width:684px;height:684px;background:radial-gradient(circle at 60% 40%,#9fd055,var(--green) 60%,#7fb834)" role="img" aria-label="Construction workers on a building site, tinted green"></div>
<div class="circle photo" style="left:512px;top:308px;width:344px;height:344px;background:linear-gradient(160deg,#eef1f3,#cfd8de 45%,#6e8fb0 75%,#b89a3c)" role="img" aria-label="Site engineer in hard hat holding a tablet"></div>
<div class="circle" style="left:458px;top:618px;width:84px;height:84px;background:var(--blue)"></div>

<header>
  <div class="abs brand"><div class="mark"></div><span>Dr. Brannock Advisory</span></div>
  <nav class="abs nav">
    <span class="active">Home</span><span>Construction</span><span>Equipment</span><span>Design</span><span>Traning</span><span>Team</span><span>Contact</span><span>imprint</span>
  </nav>
</header>

<h1 class="abs hero-title">Engineering And<br>Construction<br>Business</h1>
<p class="abs hero-sub">We develop strategies but work also in<br>critical projects to get them right.</p>
<div class="btn" style="left:78px;top:447px;width:197px;height:50px"><span>Contact Us</span><span class="arrow"><svg width="18" height="10" viewBox="0 0 18 10"><path d="M0 5h16M12 1l4 4-4 4" stroke="#fff" stroke-width="1.6" fill="none"/></svg></span></div>
<div class="abs pager"><i></i><i></i><i class="on"></i><i></i><i></i></div>

<!-- about -->
<div class="abs about-mark" role="img" aria-label="Dr. Brannock Advisory name mark">
  <div class="circle" style="position:static;width:44px;height:44px;background:var(--green);flex:none"></div>
  <b>Dr. Brannock<br>Advisory</b>
</div>
<div class="abs eyebrow" style="left:637px;top:798px">Welcome To</div>
<h2 class="abs h2" style="left:639px;top:826px;font-size:39px">Dr. Brannock Advisory</h2>
<div class="abs about-copy">
  <p>Lorem Ipsum is simply dummy text of the printing and typesetting industry. Lorem Ipsum has been the industry's standard dummy text ever since the.</p>
  <p>Lorem Ipsum is simply dummy text of the printing and typesetting industry. Lorem Ipsum has been the industry's standard dummy text ever since the, when an unknown printer took a galley of type &amp; scrambled.</p>
</div>
<div class="btn" style="left:640px;top:1112px;width:198px;height:51px"><span>Learn More</span><span class="arrow"><svg width="18" height="10" viewBox="0 0 18 10"><path d="M0 5h16M12 1l4 4-4 4" stroke="#fff" stroke-width="1.6" fill="none"/></svg></span></div>
<div class="circle" style="left:1078px;top:1105px;width:270px;height:330px;background:linear-gradient(200deg,#e6eef8,#f8fafd)"></div>

<!-- services -->
<div class="circle photo" style="left:-377px;top:1281px;width:732px;height:731px;background:radial-gradient(circle at 40% 50%,#9ccd52,var(--green) 65%,#83bc36)" role="img" aria-label="Construction site imagery tinted green"></div>
<div class="abs eyebrow" style="left:0;width:1200px;text-align:center;top:1322px">Why Us</div>
<h2 class="abs h2" style="left:0;width:1200px;text-align:center;top:1350px;font-size:40px">What We Do</h2>

<div class="card" style="left:100px"><div class="pic" style="background:linear-gradient(180deg,#dfe9ea 0,#c9d6a0 55%,#cfd3d3 70%)" role="img" aria-label="Cranes lifting large yellow letters"></div><h3>Lean Construction</h3><p>Lorem Ipsum is simply dummy text of the printing and typesetting.</p><a>Read More ▸</a></div>
<div class="card" style="left:354px"><div class="pic" style="background:linear-gradient(135deg,#8a8a8a,#3e3e3e 55%,#3a9ad6)" role="img" aria-label="Metal and blue gears"></div><h3>Lean Equipment</h3><p>Lorem Ipsum is simply dummy text of the printing and typesetting.</p><a>Read More ▸</a></div>
<div class="card" style="left:610px"><div class="pic" style="background:linear-gradient(180deg,#f1f0ec,#e6dcc6 55%,#e9a33a)" role="img" aria-label="Hands drafting a plan with ruler"></div><h3>Lean Design</h3><p>Lorem Ipsum is simply dummy text of the printing and typesetting.</p><a>Read More ▸</a></div>
<div class="card" style="left:866px"><div class="pic" style="background:linear-gradient(180deg,#b7cbe0,#a9a79d 55%,#d7c63a)" role="img" aria-label="Workers reviewing plans at a building site"></div><h3>Lean Training</h3><p>Lorem Ipsum is simply dummy text of the printing and typesetting.</p><a>Read More ▸</a></div>

<div class="circle" style="left:300px;top:1925px;width:84px;height:84px;background:var(--blue)"></div>

<!-- team -->
<h2 class="abs h2" style="left:110px;top:2174px;font-size:42px">Meet Our Team</h2>
<p class="abs" style="left:112px;top:2231px;font-size:14px;line-height:27px">Lorem Ipsum is simply dummy text of the printing and<br>typesetting industry Lorem Ipsum has.</p>
<div class="circle" style="left:115px;top:2313px;width:41px;height:41px;background:var(--green)"><svg width="41" height="41" viewBox="0 0 41 41"><path d="M23 13l-7 7.5 7 7.5" stroke="#fff" stroke-width="1.6" fill="none"/></svg></div>
<div class="circle" style="left:168px;top:2313px;width:41px;height:41px;border:1.5px solid var(--green)"><svg width="38" height="38" viewBox="0 0 38 38"><path d="M16 12l7 7-7 7" stroke="#8cc63f" stroke-width="1.6" fill="none"/></svg></div>

<div class="member" style="left:626px"><div class="face" style="background:linear-gradient(180deg,#e6e4df,#d3c7b8)" role="img" aria-label="Portrait of team member"></div><h4>Member Name</h4><p>Lorem Ipsum is simply dummy text of the printing and typesetting</p><div class="soc" role="img" aria-label="Social profile"></div></div>
<div class="member" style="left:884px"><div class="face" style="background:linear-gradient(180deg,#d7ddd6,#b9c2b8)" role="img" aria-label="Portrait of team member"></div><h4>Member Name</h4><p>Lorem Ipsum is simply dummy text of the printing and typesetting</p><div class="soc" role="img" aria-label="Social profile"></div></div>

<!-- contact band -->
<svg class="abs" style="left:0;top:2440px" width="1200" height="760" viewBox="0 0 1200 760" role="img" aria-label="Worker with safety goggles, tinted green">
  <defs><linearGradient id="band" x1="0" y1="0" x2="1" y2="1"><stop offset="0" stop-color="#93c949"/><stop offset=".5" stop-color="#8cc63f"/><stop offset="1" stop-color="#9ccd55"/></linearGradient></defs>
  <path d="M0 61 Q600 360 1200 61 V745 Q600 430 0 745 Z" fill="url(#band)"/>
</svg>
<div class="circle" style="left:180px;top:2455px;width:340px;height:300px;background:radial-gradient(circle,#f1f5fb 30%,rgba(241,245,251,0) 72%)"></div>
<h2 class="abs" style="left:0;width:1200px;text-align:center;top:2752px;font-family:'Montserrat',sans-serif;font-weight:600;font-size:34px;line-height:44px;color:var(--white)">If You Have an Any Question For<br>Contact Us Today!</h2>
<div class="btn" style="left:496px;top:2864px;width:208px;height:51px"><span>Contact Us</span><span class="arrow"><svg width="18" height="10" viewBox="0 0 18 10"><path d="M0 5h16M12 1l4 4-4 4" stroke="#fff" stroke-width="1.6" fill="none"/></svg></span></div>

<!-- footer -->
<footer>
  <div class="abs" style="left:120px;top:3195px;width:130px;text-align:center;font-weight:600;font-size:18px;line-height:24px;color:var(--blue)">Dr. Brannock<br>Advisory</div>
  <div class="circle" style="left:118px;top:3292px;width:40px;height:40px;background:var(--green)" role="img" aria-label="Social link"></div>
  <div class="circle" style="left:165px;top:3292px;width:40px;height:40px;background:var(--green)" role="img" aria-label="Social link"></div>
  <div class="circle" style="left:213px;top:3292px;width:40px;height:40px;background:var(--green)" role="img" aria-label="Social link"></div>

  <div class="abs f-title" style="left:349px;top:3137px">Sitemap</div>
  <ul class="abs f-list" style="left:345px;top:3178px">
    <li>Construction</li><li>Equipment</li><li>Design</li><li>Traning</li><li>Team</li><li>Contact</li>
  </ul>

  <div class="abs f-title" style="left:594px;top:3137px">Get In Touch</div>
  <svg class="abs" style="left:594px;top:3186px" width="18" height="26" viewBox="0 0 18 26"><path d="M9 1a8 8 0 0 0-8 8c0 6 8 16 8 16s8-10 8-16a8 8 0 0 0-8-8z" fill="var(--blue)"/><circle cx="9" cy="9" r="3" fill="#fff"/></svg>
  <p class="abs" style="left:629px;top:3182px;font-size:14px;line-height:25px;color:#333">Dr. Brannock Advisory<br>101 - Lorem ipsum text<br>print type industry</p>
  <svg class="abs" style="left:594px;top:3284px" width="20" height="15" viewBox="0 0 20 15"><rect width="20" height="15" rx="2" fill="var(--blue)"/><path d="M1 2l9 7 9-7" stroke="#fff" stroke-width="1.5" fill="none"/></svg>
  <p class="abs" style="left:629px;top:3281px;font-size:14px;color:#333">info@brannock.example</p>
  <svg class="abs" style="left:595px;top:3323px" width="18" height="18" viewBox="0 0 24 24"><path d="M6.6 10.8a15 15 0 0 0 6.6 6.6l2.2-2.2a1 1 0 0 1 1-.25 11 11 0 0 0 3.6.6 1 1 0 0 1 1 1V20a1 1 0 0 1-1 1A17 17 0 0 1 3 4a1 1 0 0 1 1-1h3.5a1 1 0 0 1 1 1 11 11 0 0 0 .6 3.6 1 1 0 0 1-.25 1z" fill="var(--blue)"/></svg>
  <p class="abs" style="left:629px;top:3322px;font-size:14px;letter-spacing:1px;color:#333">123 456 7890</p>

  <div class="abs f-title" style="left:880px;top:3137px">Newsletter</div>
  <p class="abs" style="left:879px;top:3175px;font-size:14px;line-height:25px;color:#333">Would you like to receive our<br>exclusive update for signup !</p>
  <div class="abs" style="left:878px;top:3236px;width:244px;height:46px;border:1px solid #ddd;border-radius:23px;font-size:14px;color:#555;padding:13px 0 0 19px">Enter Email *</div>
  <div class="btn" style="left:881px;top:3292px;width:178px;height:46px;font-size:17px"><span>Subscribe</span><span class="arrow" style="width:36px;height:36px"><svg width="16" height="10" viewBox="0 0 18 10"><path d="M0 5h16M12 1l4 4-4 4" stroke="#fff" stroke-width="1.6" fill="none"/></svg></span></div>

  <div class="abs" style="left:78px;top:3393px;width:1044px;height:1px;background:#e6e6e6"></div>
  <p class="abs" style="left:0;width:1200px;text-align:center;top:3414px;font-size:13px;color:#555">© <span style="color:var(--green)">Dr. Brannock Advisory</span> - 2020 All Rights reserved</p>
</footer>

</body>
</html>
```